Startup Consultancy - Brochure Design

This needs to be a digital and potential hardcopy of a glossy brochure, designed to really catch the eye of prospective clients and draw them in. I am looking for something alternative from the "usual", but equally in keeping with the IT industry that the business operate in. The business specifically focuses on Print & Document Software and Technology solutions, and this should be considered in the design.

Target Market(s)

SMB and Corporate End Users, + Technology Resellers

Industry/Entity Type

Information Technology

Other font styles liked:
• Avenir

Colors
9d9d9d
848484
c3c3c3
e8e8e8
ffffff
eaeaea
0255a3
3176b5
85acd3

Requirements
Must have
• Company logo displayed on the front, plus any other relevant placements in pages
• Must follow the colour/style in some way of the website (www.brantwellconsultancy.co.uk)
Nice to have
• Some kind of infographical style in the brochure would be good, perhaps around the service listings

```html
<!DOCTYPE html>
<html lang="en">
<head>
<meta charset="utf-8">
<title>Brantwell Consultancy – Brochure Spread</title>
<link href="https://fonts.googleapis.com/css2?family=Montserrat:wght@300;700&family=Roboto:ital,wght@0,400;0,700;1,400;1,700&display=swap" rel="stylesheet">
<style>
:root{
  --stage:#d4d4d6;
  --paper:#ffffff;
  --ink:#2e3240;
  --heading:#3b4052;
  --slate:#4b5064;
  --slate-deep:#3c4152;
  --band:#434859;
  --band-light:#c3c3c3;
  --pill:#8a90a6;
  --box:rgba(160,163,172,.82);
  --box-edge:#e8e8e8;
  --strip:#9d9d9d;
  --white:#ffffff;
}
*{margin:0;padding:0;box-sizing:border-box}
html,body{width:1200px;height:972px;overflow:hidden}
body{background:var(--stage);position:relative;font-family:"Roboto",Arial,sans-serif;color:var(--ink)}
.spread{position:absolute;left:153px;top:167px;width:895px;height:638px;background:var(--paper)}
.page-left{position:absolute;left:0;top:0;width:447px;height:626px;background:var(--paper)}
.page-right{position:absolute;left:447px;top:0;width:448px;height:626px;background:var(--slate);overflow:hidden}
.footer-strip{position:absolute;left:0;top:626px;width:895px;height:12px;background:var(--strip)}

.photo-handshake{position:absolute;left:0;top:0;width:447px;height:176px;
  background:linear-gradient(180deg,#3d3f6e 0%,#6c6f9c 35%,#b9b4c8 62%,#e9d6c2 80%,#cfcbd6 100%);
  clip-path:polygon(0 0,100% 0,100% 138px,0 176px)}
.slant-left{position:absolute;left:0;top:0}
.title-about{position:absolute;left:30px;top:128px;font-family:"Montserrat",Arial,sans-serif;font-size:27px;color:var(--white);font-weight:300;letter-spacing:.5px}
.title-about b,.title-why b,.title-how b{font-weight:700}

.copy{position:absolute;left:30px;width:386px;font-size:8.6px;line-height:10.6px;text-align:justify;color:#333}
.copy p{margin-bottom:10.6px}
.copy h3{font-size:11.5px;font-weight:700;color:var(--heading);margin-bottom:3px;text-align:left}
.copy-about{top:184px}
.copy-why{top:449px}

.banner-why{position:absolute;left:0;top:409px}
.title-why{position:absolute;left:28px;top:412px;font-family:"Montserrat",Arial,sans-serif;font-size:20px;color:var(--white);font-weight:300}

.photo-office{position:absolute;left:0;top:0;width:448px;height:165px;
  background:linear-gradient(180deg,#2f3a56 0%,#4a5877 55%,#5e6b86 100%)}
.title-how{position:absolute;left:22px;top:22px;font-family:"Montserrat",Arial,sans-serif;font-size:20px;color:var(--white);font-weight:300}
.intro{position:absolute;left:22px;top:54px;width:405px;font-size:8.8px;line-height:10.8px;color:var(--white)}
.intro p{margin-bottom:10.8px}
.slant-right{position:absolute;left:0;top:0}
.services-title{position:absolute;left:24px;top:172px;font-size:12px;font-style:italic;color:var(--white)}
.services-title b{font-weight:700}

.photo-team{position:absolute;left:0;top:420px;width:448px;height:206px;
  background:linear-gradient(180deg,rgba(75,80,100,0) 0%,#8a8f9e 35%,#aeb2bc 60%,#6f7486 100%)}

.service{position:absolute;top:198px;width:130px}
.service-icon{display:block;margin:0 auto;width:54px;height:54px}
.service-label{margin:7px auto 0;height:18px;border-radius:9px;background:var(--pill);color:var(--white);font-size:9.5px;font-weight:700;text-align:center;line-height:18px;padding:0 8px;width:max-content}
.service-box{margin-top:10px;background:var(--box);border:1.5px solid var(--box-edge);border-radius:7px;padding:5px 6px;font-size:7.2px;line-height:9.2px;font-style:italic;color:var(--white);text-align:justify}
.service-box + .service-box{margin-top:5px}
.service-strategy{left:18px}
.service-operational{left:159px}
.service-training{left:299px}

.web{position:absolute;left:0;width:448px;top:602px;text-align:center;font-size:9.5px;letter-spacing:3px;color:var(--white)}
</style>
</head>
<body>
<div class="spread">
  <section class="page-left">
    <div class="photo-handshake" role="img" aria-label="Handshake between two business people over a city skyline at sunset"></div>
    <svg class="slant-left" width="447" height="190" viewBox="0 0 447 190">
      <polygon points="170,162 447,134 447,140 200,164" fill="#c3c3c3"/>
    </svg>
    <h2 class="title-about">ABOUT <b>US</b></h2>

    <div class="copy copy-about">
      <h3>Taking a different path</h3>
      <p>We provide services to End User organisations of various sizes, shapes and styles, ranging from SMB through to Enterprise business and even Government, across a range of vertical markets, helping to create forward thinking, future proofed strategic design for Print &amp; Document Workflow solutions - critically however as an entirely independent approach, without any affiliations to manufacturers, software houses or resellers.</p>
      <p>Our expertise, experience and services also support Channel Partners, OEM's and Distributors, providing guidance and design services for Print &amp; Document Workflow strategies, promoting a customer led focus, efficiency and our own core values of honesty and reliability.</p>
      <p>As a group of very experienced, highly skilled and senior members of the IT/Print/Document Solutions industry, we grew tired of the lack of true, un-biased and trusted advice and support within the industry that both Channel Partners and End Users alike would often receive.</p>
      <p>We don't sell hardware. We don't even sell software.</p>
      <p>We remain independent of any manufacturers and are not affiliated to any partner or dealer. What we do provide however is trusted, valuable consultancy, design and advice.</p>
    </div>

    <svg class="banner-why" width="300" height="32" viewBox="0 0 300 32">
      <polygon points="0,0 295,0 273,30 0,30" fill="#434859"/>
      <polygon points="278,30 300,0 295,0 273,30" fill="#c3c3c3"/>
    </svg>
    <h2 class="title-why">WHY CHOOSE <b>US?</b></h2>

    <div class="copy copy-why">
      <h3>An alternative and innovative approach</h3>
      <p>We take pride, satisfaction and enjoyment from providing clients with clear, non-bias advice. Our determination to stand alone in the industry without commercial affiliations or ties to ANY particular manufacturer, channel partner or software developers sets us apart from the rest.</p>
      <p>We consistently monitor the marketplace and industry, ensure we are up to speed on trends and technology as well as research and understanding, to deliver professional, experienced and justifiable advice and planning.</p>
      <p>We also maintain memberships with key industry analysts such as Veritrend, Marlow Insight and more, along with having representation on European Advisory boards with a view to positively contributing to the imaging and printing industry standards.</p>
      <p>It is our aim to be the most trusted consultancy in our industry, but to do this we have to earn it.</p>
    </div>
  </section>

  <section class="page-right">
    <div class="photo-office" role="img" aria-label="Dim modern office interior with large windows"></div>
    <svg class="slant-right" width="448" height="170" viewBox="0 0 448 170">
      <polygon points="0,155 448,135 448,165 0,170" fill="#4b5064"/>
      <polygon points="145,163 448,146 448,152 152,165" fill="#e8e8e8"/>
    </svg>
    <h2 class="title-how">HOW DO WE DO <b>THAT?</b></h2>
    <div class="intro">
      <p>Honest and open advice, transparency in our approach and the integrity to ensure we inform our clients if we cannot provide services that are either suitable or to the high standards expected by you or us - if we can't help we will tell you so openly, no fuss, no over promising.</p>
      <p>Our consultancy services also ensure you are aware and prepared for potential pitfalls, complexities and challenges associated with the world of Print &amp; Document solutions.</p>
    </div>
    <p class="services-title"><b>Services for</b> Channel Partners, OEM's or Distributors</p>

    <div class="photo-team" role="img" aria-label="Team of colleagues in discussion around a meeting table"></div>

    <div class="service service-strategy">
      <svg class="service-icon" viewBox="0 0 54 54"><circle cx="27" cy="27" r="25" fill="#3c4152" stroke="#fff" stroke-width="2"/><path d="M19 40v-6c-4-2-5-6-5-10 0-7 6-11 12-11s12 4 12 10l3 6h-3v5c0 2-1 3-3 3h-4v3z" fill="#fff"/><circle cx="26" cy="23" r="4" fill="#3c4152"/><circle cx="32" cy="29" r="2.5" fill="#3c4152"/></svg>
      <div class="service-label">STRATEGY DESIGN</div>
      <div class="service-box">Strategic design and creation for startup Channel Partners or startup divisions within established resellers trying to embed themselves in the Print &amp; Document Solutions market, with hardware, software, services or any combination of those. Let us work with you to create something sustainable and profitable.</div>
      <div class="service-box">Mid-term strategic development Services designed to assist Channel Partners in re-vamping or improving existing strategies around Print &amp; Document Solutions.</div>
    </div>

    <div class="service service-operational">
      <svg class="service-icon" viewBox="0 0 54 54"><circle cx="27" cy="27" r="25" fill="#3c4152" stroke="#fff" stroke-width="2"/><rect x="21" y="13" width="12" height="12" rx="1.5" fill="#fff"/><path d="M12 26l3 9 8 6h8l8-6 3-9-4 1-4 7h-16l-4-7z" fill="#fff"/></svg>
      <div class="service-label">OPERATIONAL DESIGN</div>
      <div class="service-box">Print &amp; Document solutions – commercial &amp; administration structure services including greenfield designs and/or improvements on existing structures for Channel Partners to create or improve efficiencies in back office processes.</div>
      <div class="service-box">Customer Service/Support structure designs and assistance. Ensuring efficient and profitable support centres. We have experience and knowledge of creating and managing support structures up to a European coverage level and can provide valuable knowledge and assistance.</div>
      <div class="service-box">Monitoring &amp; Management Software - choosing the right software for your needs, both now and in the future in line with a strategy is critical to success. We can help Channel Partners with a structured approach to due dilligence to ensure the right solution is chosen.</div>
    </div>

    <div class="service service-training">
      <svg class="service-icon" viewBox="0 0 54 54"><circle cx="27" cy="27" r="25" fill="#3c4152" stroke="#fff" stroke-width="2"/><rect x="20" y="15" width="19" height="15" fill="none" stroke="#fff" stroke-width="2"/><circle cx="16" cy="20" r="3" fill="#fff"/><path d="M13 25h6l6 3-1 2-5-2v12h-6z" fill="#fff"/><path d="M30 30l-3 8M30 30l3 8" stroke="#fff" stroke-width="1.6"/></svg>
      <div class="service-label">TRAINING SERVICES</div>
      <div class="service-box">We provide training based around Print &amp; Document solution strategy and methodology. The do's and don't's, the changing faces of the market and customer expectations and how the right approach can bring benefits.</div>
    </div>

    <p class="web">www.brantwellconsultancy.co.uk</p>
  </section>

  <div class="footer-strip"></div>
</div>
</body>
</html>
```